Customer Dashboard Design for Email Security SaaS

Mailvornet is a commercial email spam filter offered as a SaaS product, built and operated by a small German hosting provider. It protects business email accounts against spam, phishing, scam, and viruses using a multilayer filtering pipeline that combines traditional spam detection with AI-powered classification. The product runs entirely on German infrastructure, ensuring data sovereignty for European customers.

We need a complete redesign of the customer-facing dashboard. This is the web application where paying customers manage their email filtering: view their mail log, check quarantined emails, manage allow/blocklists, configure their settings, and handle their subscription. It is the primary touchpoint between Mailvornet and its customers.

Our customers are system administrators, IT managers at small-to-medium businesses, and operators of small hosting providers. They are technically competent but not designers. They expect professional, efficient tools that respect their time. They typically manage 10–500 email accounts and check the dashboard a few times per week, with heavier use during spam incidents.

We have attached the current mockups which really need to be replaced with something good looking.

Target Market(s)

System administrators, IT managers at small-to-medium businesses, and operators of small hosting providers.

Industry/Entity Type

SaaS

Number of Pages Required

5+ page

```html
<!DOCTYPE html>
<html lang="en">
<head>
<meta charset="utf-8">
<title>Mailvornet – Allowlist</title>
<link href="https://fonts.googleapis.com/css2?family=DM+Sans:wght@400;500;600&family=Source+Serif+4:opsz,wght@8..60,600;8..60,700&family=JetBrains+Mono:wght@400&display=swap" rel="stylesheet">
<style>
:root{
  --bg:#1a1310;
  --sidebar:#1c1512;
  --line:#33271f;
  --line-soft:#2c221c;
  --card:#211915;
  --card-head:#261d18;
  --notice-bg:#261a10;
  --notice-line:#4a331d;
  --input:#2b221d;
  --accent:#e08c2b;
  --accent-dim:#8c5a1f;
  --accent-text:#f3c58a;
  --text:#f2ebe6;
  --muted:#a89b92;
  --faint:#7d7069;
  --danger:#e0423a;
  --danger-bg:#3a1c18;
  --chip:#332821;
}
*{box-sizing:border-box;margin:0;padding:0}
html,body{width:1200px;height:731px;overflow:hidden;background:var(--bg);color:var(--text);font-family:"DM Sans",sans-serif}
.app{display:flex;width:1200px;height:731px}
.sidebar{width:198px;height:100%;background:var(--sidebar);border-right:1px solid var(--line);display:flex;flex-direction:column}
.brand{height:68px;display:flex;align-items:center;gap:10px;padding-left:19px;border-bottom:1px solid var(--line)}
.brand-mark{width:31px;height:31px;border-radius:8px;background:var(--accent)}
.brand-name{font-family:"Source Serif 4",serif;font-weight:700;font-size:15.5px;color:var(--text)}
.nav{padding:12px 12px 0;display:flex;flex-direction:column;gap:3px}
.nav-item{height:37px;display:flex;align-items:center;gap:11px;padding-left:13px;border-radius:8px;font-size:12.5px;color:var(--text)}
.nav-item svg{width:14px;height:14px;stroke:currentColor;fill:none;stroke-width:1.8;stroke-linecap:round;stroke-linejoin:round}
.nav-item.active{background:var(--accent);color:#2a1a08}
.sidebar-foot{margin-top:auto;border-top:1px solid var(--line);padding:12px 12px 14px;display:flex;flex-direction:column;gap:8px}
.user-card{background:#2a211c;border-radius:8px;padding:10px 13px;height:47px}
.user-name{font-size:11.5px;font-weight:500}
.user-mail{font-size:9px;color:var(--muted);margin-top:2px}
.main{flex:1;padding:22px 30px 0 31px}
.page-title{font-family:"Source Serif 4",serif;font-weight:700;font-size:29px;line-height:36px}
.page-sub{font-size:12.5px;color:var(--muted);margin-top:5px}
.notice{margin-top:19px;height:84px;border:1px solid var(--notice-line);background:var(--notice-bg);border-radius:10px;padding:13px 14px;display:flex;gap:10px}
.notice svg{width:14px;height:14px;stroke:var(--accent);fill:none;stroke-width:1.8;margin-top:2px;flex:none}
.notice-lead{font-size:11px;line-height:16px}
.notice-hint{font-size:10.5px;color:var(--muted);margin:3px 0 0 15px;line-height:16px}
code{font-family:"JetBrains Mono",monospace;font-size:9.5px;background:var(--chip);color:#c9bdb4;padding:1px 4px;border-radius:3px}
.add-card{margin-top:18px;height:106px;border:1px solid var(--line);background:var(--card);border-radius:12px;padding:20px 18px}
.card-title{font-family:"Source Serif 4",serif;font-weight:700;font-size:14.5px}
.add-row{display:flex;gap:10px;margin-top:13px}
.add-input{flex:1;height:32px;border:1px solid var(--line);background:var(--input);border-radius:7px;padding-left:12px;display:flex;align-items:center;font-size:12.5px;color:var(--faint)}
.add-btn{width:81px;height:32px;border-radius:7px;background:var(--accent-dim);color:var(--accent-text);display:flex;align-items:center;justify-content:center;gap:6px;font-size:12.5px;font-weight:500}
.add-btn svg{width:11px;height:11px;stroke:currentColor;stroke-width:2;fill:none}
.section-title{font-family:"Source Serif 4",serif;font-weight:700;font-size:14.5px;margin-top:19px}
.senders{margin-top:11px;border:1px solid var(--line);border-radius:10px;overflow:hidden;background:var(--card)}
.row{display:grid;grid-template-columns:467px 1fr 60px;align-items:center;padding-left:18px;border-top:1px solid var(--line)}
.row.head{height:40px;background:var(--card-head);border-top:none;font-size:11px;color:var(--muted)}
.row.body{height:50px}
.addr{font-family:"JetBrains Mono",monospace;font-size:10px;color:var(--text)}
.date{font-size:11px;color:var(--muted)}
.del{width:25px;height:25px;border-radius:7px;background:var(--danger-bg);display:flex;align-items:center;justify-content:center}
.del svg{width:11px;height:11px;stroke:var(--danger);fill:none;stroke-width:2;stroke-linecap:round}
</style>
</head>
<body>
<div class="app">
  <aside class="sidebar">
    <div class="brand"><div class="brand-mark"></div><span class="brand-name">Mailvornet</span></div>
    <nav class="nav">
      <div class="nav-item"><svg viewBox="0 0 24 24"><rect x="3" y="3" width="7" height="9" rx="1"/><rect x="14" y="3" width="7" height="5" rx="1"/><rect x="14" y="12" width="7" height="9" rx="1"/><rect x="3" y="16" width="7" height="5" rx="1"/></svg>Dashboard</div>
      <div class="nav-item"><svg viewBox="0 0 24 24"><path d="M14 2H6a2 2 0 0 0-2 2v16a2 2 0 0 0 2 2h12a2 2 0 0 0 2-2V8z"/><path d="M14 2v6h6M8 13h8M8 17h8"/></svg>Mail Log</div>
      <div class="nav-item"><svg viewBox="0 0 24 24"><path d="M22 12h-6l-2 3h-4l-2-3H2"/><path d="M5.5 5h13L22 12v6a2 2 0 0 1-2 2H4a2 2 0 0 1-2-2v-6z"/></svg>Mailboxes</div>
      <div class="nav-item active"><svg viewBox="0 0 24 24"><path d="M12 22s8-4 8-10V5l-8-3-8 3v7c0 6 8 10 8 10z"/></svg>Allowlist</div>
      <div class="nav-item"><svg viewBox="0 0 24 24"><path d="M12 22s8-4 8-10V5l-8-3-8 3v7c0 6 8 10 8 10z"/><path d="M3 3l18 18"/></svg>Blocklist</div>
      <div class="nav-item"><svg viewBox="0 0 24 24"><rect x="2" y="3" width="20" height="5" rx="1"/><path d="M4 8v11a2 2 0 0 0 2 2h12a2 2 0 0 0 2-2V8M10 12h4"/></svg>Quarantine</div>
      <div class="nav-item"><svg viewBox="0 0 24 24"><circle cx="12" cy="12" r="3"/><path d="M12 2v3M12 19v3M2 12h3M19 12h3M4.9 4.9l2.1 2.1M17 17l2.1 2.1M4.9 19.1L7 17M17 7l2.1-2.1"/></svg>Settings</div>
      <div class="nav-item"><svg viewBox="0 0 24 24"><rect x="2" y="5" width="20" height="14" rx="2"/><path d="M2 10h20"/></svg>Billing</div>
    </nav>
    <div class="sidebar-foot">
      <div class="nav-item"><svg viewBox="0 0 24 24"><circle cx="12" cy="12" r="4"/><path d="M12 2v2M12 20v2M2 12h2M20 12h2M4.9 4.9l1.4 1.4M17.7 17.7l1.4 1.4M4.9 19.1l1.4-1.4M17.7 6.3l1.4-1.4"/></svg>Light Mode</div>
      <div class="user-card"><div class="user-name">Admin User</div><div class="user-mail">admin@example.com</div></div>
      <div class="nav-item"><svg viewBox="0 0 24 24"><path d="M9 21H5a2 2 0 0 1-2-2V5a2 2 0 0 1 2-2h4M16 17l5-5-5-5M21 12H9"/></svg>Logout</div>
    </div>
  </aside>
  <main class="main">
    <h1 class="page-title">Allowlist</h1>
    <p class="page-sub">Email addresses and domains that should always be delivered, even if flagged as spam</p>
    <div class="notice">
      <svg viewBox="0 0 24 24"><path d="M12 22s8-4 8-10V5l-8-3-8 3v7c0 6 8 10 8 10z"/></svg>
      <div>
        <p class="notice-lead">Add email addresses or domains to the allowlist to ensure they're never blocked.</p>
        <p class="notice-hint">Use full email: <code>user@example.com</code></p>
        <p class="notice-hint">Use domain wildcard: <code>@example.com</code></p>
      </div>
    </div>
    <section class="add-card">
      <h2 class="card-title">Add to Allowlist</h2>
      <div class="add-row">
        <div class="add-input">email@example.com or @domain.com</div>
        <div class="add-btn"><svg viewBox="0 0 12 12"><path d="M6 1v10M1 6h10"/></svg>Add</div>
      </div>
    </section>
    <h2 class="section-title">Allowed Senders (3)</h2>
    <div class="senders">
      <div class="row head"><span>Email / Domain</span><span>Date Added</span><span></span></div>
      <div class="row body"><span class="addr">trusted@vendoro.net</span><span class="date">2024-02-15</span><span class="del"><svg viewBox="0 0 12 12"><path d="M1.5 3h9M4.5 3V1.5h3V3M2.5 3l.6 7.5h5.8L9.5 3M5 5v3.5M7 5v3.5"/></svg></span></div>
      <div class="row body"><span class="addr">@brightlane-media.com</span><span class="date">2024-03-08</span><span class="del"><svg viewBox="0 0 12 12"><path d="M1.5 3h9M4.5 3V1.5h3V3M2.5 3l.6 7.5h5.8L9.5 3M5 5v3.5M7 5v3.5"/></svg></span></div>
      <div class="row body"><span class="addr">newsletter@tidepost.io</span><span class="date">2024-03-22</span><span class="del"><svg viewBox="0 0 12 12"><path d="M1.5 3h9M4.5 3V1.5h3V3M2.5 3l.6 7.5h5.8L9.5 3M5 5v3.5M7 5v3.5"/></svg></span></div>
    </div>
  </main>
</div>
</body>
</html>
```